Wedding Invitation and Logo

We would like an invitation and logo designed for our wedding on October 19, 2019 in Charlotte, NC. Our names are Tess and Hank, we met in school at Brindlewood Ridge University, and we got engaged at a fire tower which has a view down to the campus. You do not have to include these, but some ideas for the invitation design would be mountains, a fire tower, our initials, or the city. The wedding will be at 4:30 in the afternoon with a reception to follow. We do not need to list the families as there are four of them and that is too much info. The colors we would like to use are white, black, royal blue, and maybe silver. Do not feel obligated to use them all though.We would like the logo to include similar elements such as mountains, fire tower, or our initials(T and H). The logo can be a one color design as we may use it on our cake, as light filters to be displayed on the walls at our reception, or as an accent on name plates and stationery.We like simple, clean designs and our wedding will have a wintery theme (white linens, white chair covers, silver and royal blue accents, etc.).Things we do not want: snowflakes, flowers, polka dots, leaves, gold foil.Thank you!

Font styles to use
Serif
Script

Requirements
Must have
• Some combination of white, black, royal blue, optionally silver.
Nice to have
• Mountains, fire tower, our initials (T and H), wintry theme (no snowflakes)
Should not have
• Snowflakes, flowers, polka dots, leaves, gold foil

```html
<!DOCTYPE html>
<html lang="en">
<head>
<meta charset="utf-8">
<title>Tess &amp; Hank Wedding Invitation</title>
<link href="https://fonts.googleapis.com/css2?family=Cinzel:wght@400&family=Parisienne&display=swap" rel="stylesheet">
<style>
  :root {
    --page: #ffffff;
    --band: #c4c8cc;
    --panel: #eeeeee;
    --navy: #1d3763;
    --rule: #8a8a8a;
    --ornament: #9a9a9a;
    --skyline-top: #e2e2e2;
    --skyline-bottom: #d2d2d2;
  }
  * { margin: 0; padding: 0; box-sizing: border-box; }
  html, body {
    width: 1200px; height: 1200px; overflow: hidden;
    background: var(--page);
  }
  .canvas { position: relative; width: 1200px; height: 1200px; }
  .invitation {
    position: absolute; left: 320px; top: 179px;
    width: 559px; height: 782px;
    background: var(--band);
  }
  .invitation__panel {
    position: absolute; left: 30px; top: 30px;
    width: 499px; height: 722px;
    background: var(--panel);
  }
  .invitation__frame {
    position: absolute; left: 0; top: 0; width: 1200px; height: 1200px;
    pointer-events: none;
  }
  .ornament, .skyline {
    position: absolute;
  }
  .ornament--corner-left { left: 368px; top: 228px; width: 46px; height: 46px; background: var(--ornament); opacity: .35; }
  .ornament--corner-right { left: 786px; top: 228px; width: 46px; height: 46px; background: var(--ornament); opacity: .35; }
  .ornament--divider { left: 559px; top: 796px; width: 91px; height: 14px; background: var(--ornament); opacity: .6; border-radius: 7px; }
  .skyline {
    left: 374px; top: 818px; width: 451px; height: 99px;
    background: linear-gradient(to bottom, var(--skyline-top), var(--skyline-bottom));
  }
  .text { position: absolute; left: 350px; width: 499px; text-align: center; color: var(--navy); }
  .monogram {
    top: 262px; font-family: "Parisienne", cursive; font-size: 56px; line-height: 1;
  }
  .invite-line {
    top: 433px; font-family: "Parisienne", cursive; font-size: 27px; line-height: 1;
  }
  .couple {
    top: 518px; font-family: "Cinzel", serif; font-size: 46px; letter-spacing: 9px; line-height: 1;
    padding-left: 9px;
  }
  .details {
    top: 606px; font-family: "Cinzel", serif; font-size: 23px; line-height: 30px;
  }
  .reception-line {
    top: 753px; font-family: "Parisienne", cursive; font-size: 27px; line-height: 1;
  }
</style>
</head>
<body>
<main class="canvas">
  <section class="invitation" aria-label="Wedding invitation">
    <div class="invitation__panel"></div>
  </section>

  <svg class="invitation__frame" viewBox="0 0 1200 1200" aria-hidden="true">
    <line x1="418" y1="230" x2="782" y2="230" stroke="var(--rule)" stroke-width="1"/>
    <line x1="374" y1="278" x2="374" y2="868" stroke="var(--rule)" stroke-width="1"/>
    <line x1="825" y1="278" x2="825" y2="868" stroke="var(--rule)" stroke-width="1"/>
  </svg>

  <div class="ornament ornament--corner-left" role="img" aria-label="Scrolled corner ornament"></div>
  <div class="ornament ornament--corner-right" role="img" aria-label="Scrolled corner ornament"></div>

  <div class="text monogram">T and H</div>
  <p class="text invite-line">Kindly join us for the wedding of</p>
  <h1 class="text couple" style="font-weight:400">TESS &amp; HANK</h1>
  <p class="text details">October 19, 2019<br>4:30 In The Afternoon<br>Charlotte, NC</p>
  <p class="text reception-line">Dinner and dancing to follow</p>

  <div class="ornament ornament--divider" role="img" aria-label="Small scrolled divider ornament"></div>
  <div class="skyline" role="img" aria-label="Line drawing of the Charlotte city skyline"></div>
</main>
</body>
</html>
```